Advertisement Design Project

Attached is the information I need in a big color ad

10X11 that will go in a weekly local paper.
I am open to color and graphics-no pictures of people please.

My logo is also attached, which I would like in the ad.

Sorry for the short notice-I just got a deal on the space and it is due Friday.

```html
<!DOCTYPE html>
<html lang="en">
<head>
<meta charset="utf-8">
<title>New Tax Laws – Estate Planning Workshop</title>
<link rel="stylesheet" href="https://fonts.googleapis.com/css2?family=Open+Sans:wght@400;600;700&family=Saira+Semi+Condensed:wght@400&display=swap">
<style>
  :root {
    --red: #f2383a;
    --red-dark: #c9282b;
    --yellow: #fbb418;
    --gold: #fbb824;
    --blue: #1747f0;
    --white: #ffffff;
    --ink: #111111;
    --cream: #fbd98a;
    --shadow: #9c1f22;
  }
  * { box-sizing: border-box; margin: 0; padding: 0; }
  html, body {
    width: 1095px; height: 1200px; overflow: hidden;
    background: var(--red);
    font-family: "Open Sans", Arial, sans-serif;
  }
  .page { position: relative; width: 1095px; height: 1200px; overflow: hidden; background: var(--red); }
  .abs { position: absolute; }
  .fit { display: block; overflow: visible; }
  .fit text { font-family: "Saira Semi Condensed", "Arial Narrow", sans-serif; }

  .headline { left: 0; top: 0; width: 1095px; height: 200px; }
  .headline .shadow { fill: var(--shadow); opacity: .55; }
  .headline .face { fill: var(--gold); }

  .info-band { left: 0; top: 273px; width: 1095px; height: 534px; background: var(--yellow); }
  .trusts-tab {
    left: 0; top: 207px; width: 513px; height: 106px; background: var(--blue);
    color: var(--white); font-weight: 700; font-size: 82px; line-height: 106px; padding-left: 78px;
  }

  .topics { left: 40px; top: 318px; width: 560px; color: var(--blue); }
  .topics-title { font-weight: 700; font-size: 44px; line-height: 52px; }
  .topic-list { list-style: none; margin-top: 8px; font-size: 18.5px; line-height: 26.4px; }
  .topic-list li { position: relative; padding-left: 13px; }
  .topic-list li::before { content: "•"; position: absolute; left: 0; }
  .cta { left: 40px; top: 762px; font-weight: 700; font-size: 26px; line-height: 32px; color: var(--ink); }

  .about-panel { left: 607px; top: 263px; width: 433px; height: 544px; background: var(--blue); }
  .about-lede { left: 20px; top: 20px; color: var(--gold); font-weight: 700; font-size: 40px; line-height: 52px; white-space: nowrap; }
  .value {
    left: 44px; width: 305px; height: 50px; border: 2px solid #b9c6f5; border-radius: 13px;
    color: var(--white); font-weight: 600; font-size: 25px; line-height: 46px; padding-left: 64px;
  }
  .value::before {
    content: ""; position: absolute; left: 18px; top: 13px; width: 21px; height: 21px; border-radius: 50%;
    background: radial-gradient(circle at 40% 40%, #fff6a0, #f2c200 60%, #c99200);
  }
  .presenter { left: 41px; top: 424px; color: var(--white); font-size: 21px; line-height: 25px; }
  .presenter strong { font-weight: 700; }

  .schedule { left: 37px; top: 825px; width: 547px; height: 76px; border: 3px solid var(--red-dark); display: flex; }
  .schedule-label { width: 220px; background: var(--red-dark); color: var(--white);
    font-weight: 700; font-size: 24px; line-height: 29px; padding: 8px 0 0 45px; }
  .schedule-times { color: var(--white); font-size: 24px; line-height: 29px; padding: 5px 0 0 29px; }

  .reserve-note { left: 40px; top: 916px; color: var(--gold); font-weight: 700; font-size: 22.5px; white-space: nowrap; }
  .phone { left: 37px; top: 950px; width: 560px; height: 80px; }
  .phone text { fill: var(--gold); font-family: "Open Sans", Arial, sans-serif !important; }
  .venue { left: 40px; top: 1031px; color: var(--white); font-size: 22.5px; line-height: 32px; white-space: nowrap; }

  .brand { left: 693px; top: 918px; width: 267px; text-align: center; color: var(--cream); font-weight: 700; font-size: 32px; }
  .brand-dot { display: block; margin: 0 auto 14px; width: 40px; height: 40px; border-radius: 50%; background: var(--cream); }

  .motto { left: 0; top: 1104px; width: 604px; height: 76px; background: var(--blue); }
  .motto text { fill: var(--gold); }
  .tagline { left: 604px; top: 1104px; width: 491px; height: 76px; background: var(--yellow); }
  .tagline text { fill: var(--ink); }
</style>
</head>
<body>
<div class="page">
  <svg class="abs fit headline" viewBox="0 0 1095 200" width="1095" height="200" aria-label="New Tax Laws">
    <text class="shadow" x="86" y="176" font-size="200" textLength="941" lengthAdjust="spacingAndGlyphs">New Tax Laws</text>
    <text class="face" x="83" y="173" font-size="200" textLength="941" lengthAdjust="spacingAndGlyphs">New Tax Laws</text>
  </svg>

  <div class="abs info-band"></div>
  <div class="abs trusts-tab">Trusts</div>

  <section class="abs topics">
    <h2 class="topics-title">Annuities and<br>Long Term Care</h2>
    <ul class="topic-list">
      <li>Is a living Trust right for me?</li>
      <li>Does my existing Trust need to be changed?</li>
      <li>Why does Joint Tenancy create tax problems?</li>
      <li>I have a Will, isn't that enough?</li>
      <li>Why do I need powers of attorney?</li>
      <li>How much are inheritance taxes?</li>
      <li>What are the new Affordable Care Act Taxes?</li>
      <li>How does Long Term Care insurance work?</li>
      <li>The average cost of long term care is over 80K a year-<br>how do I plan for those costs?</li>
      <li>The truth about annuities</li>
      <li>What are the biggest mistakes in estate planning?</li>
    </ul>
  </section>
  <p class="abs cta">Come learn what you need to know</p>

  <section class="abs about-panel">
    <p class="abs about-lede">Helping &nbsp;Families<br>plan their estates<br>for over 20 years.</p>
    <div class="abs value" style="top:201px">Trust</div>
    <div class="abs value" style="top:279px">Relationship</div>
    <div class="abs value" style="top:356px">Integrity</div>
    <p class="abs presenter"><strong>Presented by:</strong><br>dana merrit holloway<br>Attorney at Law<br>2140 Alder Street, Seabrook.</p>
  </section>

  <div class="abs schedule">
    <div class="schedule-label">Workshop<br>Times:</div>
    <div class="schedule-times">September 19, 2013<br>1 - 2:30pm • 6 - 7:30pm</div>
  </div>

  <p class="abs reserve-note">Seating is limited for a Reservation please call:</p>
  <svg class="abs fit phone" viewBox="0 0 560 80" width="560" height="80" aria-label="(555) 014-2760">
    <text x="3" y="66" font-size="70" textLength="555" lengthAdjust="spacingAndGlyphs">(555) 014-2760</text>
  </svg>
  <p class="abs venue">Coastline Harbor Inn<br>4810 Driftwood Court, Seabrook, California 90000</p>

  <div class="abs brand"><span class="brand-dot"></span>Holloway Law</div>

  <svg class="abs fit motto" viewBox="0 0 604 76" width="604" height="76" aria-label="Security =Good information+Good Planning">
    <text x="40" y="48" font-size="29" textLength="540" lengthAdjust="spacingAndGlyphs">Security =Good information+Good Planning</text>
  </svg>
  <svg class="abs fit tagline" viewBox="0 0 491 76" width="491" height="76" aria-label="Be Smart. Plan Ahead.">
    <text x="73" y="50" font-size="34" textLength="343" lengthAdjust="spacingAndGlyphs">Be Smart. Plan Ahead.</text>
  </svg>
</div>
</body>
</html>
```